Mental Health care Company in Washington DC

We are a new mental health care services provider in Washington DC. Please look at these sites.
https://marlowbrookpartners.com
https://www.quillstoneinc.com
https://velmarsh-kt.org/
https://www.trivanqx.com
https://www.thelanternofqz.com

```html
<!DOCTYPE html>
<html lang="en">
<head>
<meta charset="utf-8">
<title>Varden Health Services — Mental Wellness in Washington DC</title>
<link href="https://fonts.googleapis.com/css2?family=Poppins:wght@400;500;600;700&family=Great+Vibes&display=swap" rel="stylesheet">
<style>
:root{
  --navy:#0d1f45;
  --ink:#0f1d3d;
  --orange:#f5883a;
  --orange-soft:#f7a566;
  --teal:#a9dbe0;
  --grey:#5b6170;
  --line:#d9dde4;
  --white:#ffffff;
}
*{box-sizing:border-box;margin:0;padding:0}
html,body{width:1200px;height:5254px;overflow:hidden}
body{position:relative;background:var(--white);font-family:"Poppins",sans-serif;color:var(--ink)}
.abs{position:absolute}
svg{display:block}

/* top bar */
.topbar{left:480px;top:0;width:720px;height:30px;background:var(--navy);color:#fff;font-size:9.5px;display:flex;align-items:center;gap:34px;padding-left:34px}
.topbar::before{content:"";position:absolute;left:-8px;top:0;width:28px;height:30px;background:var(--orange);transform:skewX(25deg)}
.topbar span{display:flex;align-items:center;gap:6px}
.topbar i{display:inline-block;width:10px;height:10px;border-radius:50%;background:var(--orange)}

/* header */
.brand{left:141px;top:26px;font-weight:500;font-size:33px;color:var(--ink);letter-spacing:-.5px;line-height:1}
.brand-sub{left:141px;top:60px;width:168px;font-size:10px;letter-spacing:8px;color:var(--ink);text-align:center}
.nav{left:510px;top:52px;font-size:12.5px;font-weight:500}
.nav a{color:var(--ink);text-decoration:none;position:absolute;white-space:nowrap}
.nav a.active{color:var(--orange)}
.btn-contact{left:951px;top:47px;width:108px;height:31px;border-radius:16px;background:var(--orange);color:#fff;font-size:10.5px;font-weight:600;display:flex;align-items:center;justify-content:center}

/* hero */
.hero{left:0;top:92px;width:1200px;height:650px;background:linear-gradient(100deg,#2f3033 0%,#4a4b4d 40%,#8a8a88 70%,#bdbcb7 100%)}
.hero-person{left:660px;top:130px;width:360px;height:600px;border-radius:160px 160px 40px 40px;background:linear-gradient(180deg,#d9dadf 0%,#f0f0f2 45%,#c7cad3 100%);opacity:.9}
.hero-eyebrow{left:141px;top:214px;color:#fff;font-size:22px;font-weight:500;letter-spacing:.5px}
.hero-title{left:141px;top:246px;color:#fff;font-size:44px;font-weight:700;line-height:54px}
.hero-title .hl{color:var(--teal)}
.hero-title .light{font-weight:400}
.hero-text{left:141px;top:364px;width:400px;color:#fff;font-size:14px;line-height:24px}
.btn-book{left:141px;top:471px;width:200px;height:41px;border-radius:21px;background:var(--orange);color:#fff;font-size:11.5px;font-weight:600;display:flex;align-items:center;justify-content:center;gap:7px}
.scroll-btn{left:573px;top:706px;width:50px;height:50px;border-radius:50%;background:#fff;box-shadow:0 3px 10px rgba(0,0,0,.15);display:flex;align-items:center;justify-content:center}

/* section heads */
.kicker{font-size:56px;font-weight:600;color:var(--ink);line-height:1}
.headline{font-size:38px;font-weight:600;color:var(--ink);line-height:1;padding-bottom:8px;border-bottom:3px solid var(--orange);display:inline-block;white-space:nowrap}
.para{font-size:13px;line-height:22px;color:var(--grey)}

/* about */
.about-bubble{left:383px;top:824px;width:164px;height:164px;border-radius:50%;background:var(--teal)}
.about-photo-main{left:141px;top:851px;width:370px;height:370px;border-radius:50%;background:linear-gradient(160deg,#3a2c24 0%,#8a6a52 45%,#c9b7a4 80%,#e0d8cf 100%)}
.about-photo-small{left:356px;top:1085px;width:250px;height:250px;border-radius:50%;border:8px solid #fff;background:linear-gradient(180deg,#ece3d3 0%,#d8c6a8 55%,#bba27e 100%)}
.about-kicker{left:671px;top:804px}
.about-head{left:667px;top:862px}
.sub-title{font-size:23px;font-weight:600;color:var(--ink);display:flex;align-items:center;gap:10px}

/* choose */
.choose-bg{left:0;top:1420px;width:1200px;height:750px}
.choose-kicker{left:146px;top:1536px}
.choose-head{left:141px;top:1595px}
.feature-card{width:288px;height:218px;top:1770px;border:1.5px solid #7fa9b5;border-radius:16px;text-align:center;padding-top:62px}
.feature-card h3{font-size:21px;font-weight:600;color:var(--ink);line-height:27px}
.feature-card p{font-size:11.5px;line-height:21px;color:var(--grey);margin:14px 22px 0}
.feature-tab{width:139px;height:134px;top:1684px;background:var(--orange-soft);border-radius:70px 70px 14px 14px;display:flex;align-items:center;justify-content:center}

/* services */
.service-photo{left:141px;top:2280px;width:460px;height:571px;border-radius:0 230px 0 0;background:linear-gradient(180deg,#c9d6de 0%,#9fb4c2 40%,#6e8798 70%,#3e4a52 100%)}
.services-kicker{left:630px;top:2236px}
.services-head{left:627px;top:2292px}
.services-intro{left:627px;top:2356px;width:400px}
.service-panel{left:506px;top:2429px;width:553px;height:384px;background:#fff;box-shadow:0 6px 24px rgba(15,29,61,.08);padding:18px 30px 0 30px}
.service-item{display:flex;gap:22px;padding:16px 0 18px;border-bottom:1px solid #eceef2}
.service-item:last-child{border-bottom:none}
.service-item h4{font-size:17px;font-weight:600;color:var(--ink);margin-bottom:8px}
.service-item p{font-size:12px;line-height:21px;color:var(--grey)}
.service-item svg{flex:none;margin-top:8px}

/* lake */
.lake{left:0;top:2845px;width:1200px;height:540px;background:linear-gradient(180deg,#a7b6c3 0%,#8598a8 30%,#4d6478 52%,#2a4a6e 70%,#1d3a5e 100%)}

/* testimonials */
.navy-band{left:0;top:3320px;width:1200px;height:760px}
.t-kicker{left:0;top:3388px;width:1200px;text-align:center;font-size:58px;font-weight:600;color:#fff;line-height:1}
.t-head{left:391px;top:3452px;font-size:38px;font-weight:500;color:#fff;line-height:1;padding-bottom:8px;border-bottom:3px solid var(--orange);white-space:nowrap}
.t-card{top:3555px;width:275px;height:262px;border:2px solid #5a80c8;border-radius:14px;background:#16387f;padding:34px 24px 0;text-align:center}
.t-card p{font-size:11px;line-height:19.5px;font-style:italic;color:#fff}
.t-card .stars{color:var(--orange);font-size:13px;letter-spacing:2px;margin-top:2px}
.t-quote{top:3537px;width:36px;height:30px;border-radius:6px;background:var(--teal);display:flex;align-items:center;justify-content:center;font-size:26px;font-weight:700;color:var(--navy)}
.t-avatar{top:3774px;width:86px;height:86px;border-radius:50%;border:3px solid #fff;background:linear-gradient(180deg,#c9c2ba 0%,#8f857c 60%,#4e4a47 100%)}
.t-name{top:3878px;width:275px;text-align:center;color:#fff;font-size:14px;font-weight:500;line-height:18px}
.t-name small{display:block;font-size:10px;font-weight:400;color:#c7d0e3}
.t-arrow{top:3664px;width:36px;height:36px;border-radius:50%;border:1.5px solid #d0d8e8;display:flex;align-items:center;justify-content:center}

/* contact */
.c-kicker{left:0;top:4152px;width:1200px;text-align:center;font-size:56px;font-weight:600;color:var(--ink);line-height:1}
.c-head{left:0;top:4212px;width:1200px;text-align:center;font-size:38px;font-weight:600;color:var(--ink);line-height:1}
.c-head span{display:inline-block;padding-bottom:8px;border-bottom:3px solid var(--orange)}
.c-intro{left:370px;top:4276px;width:460px;text-align:center}
.footer-bg{left:0;top:4560px;width:1200px;height:694px}
.form-card{left:253px;top:4348px;width:694px;height:391px;background:#fff;border-radius:6px;box-shadow:0 8px 30px rgba(15,29,61,.10)}
.field{height:43px;border:1px solid var(--line);border-radius:3px;display:flex;align-items:center;font-size:11px;color:#4b5160}
.field .ico{width:36px;height:100%;border-right:1px solid var(--line);display:flex;align-items:center;justify-content:center;margin-right:10px}
.field.area{height:84px;align-items:flex-start}
.field.area .ico{height:34px}
.field.area span{padding-top:11px}
.btn-submit{left:516px;top:4640px;width:151px;height:38px;border-radius:19px;background:var(--orange);color:var(--ink);font-size:12px;font-weight:600;display:flex;align-items:center;justify-content:flex-end;padding-right:8px;gap:18px}
.btn-submit i{width:28px;height:28px;border-radius:50%;border:1.5px solid var(--ink);display:flex;align-items:center;justify-content:center;font-style:normal}

/* footer */
.sub-script{left:141px;top:4790px;font-family:"Great Vibes",cursive;font-size:40px;color:#fff;line-height:1}
.sub-title-f{left:141px;top:4828px;font-size:34px;font-weight:600;color:#fff;line-height:1.1}
.sub-input{left:647px;top:4815px;width:412px;height:40px;border-bottom:1px solid #5c6c8e;color:#fff;font-size:11.5px;display:flex;align-items:center;justify-content:space-between}
.sub-input b{font-weight:600;display:flex;align-items:center;gap:12px}
.sub-input b i{width:26px;height:26px;border-radius:50%;border:1px solid #fff;display:flex;align-items:center;justify-content:center;font-style:normal;font-size:12px}
.f-col h5{font-size:16px;font-weight:600;color:#fff;padding-bottom:8px;border-bottom:2px solid var(--orange);display:inline-block;margin-bottom:16px}
.f-col ul{list-style:none;font-size:12px;color:#fff;line-height:28px}
.f-col .det{display:flex;gap:12px;color:#fff;font-size:12px;line-height:19px;margin-bottom:14px}
.f-col .det b{font-weight:600;font-size:11.5px}
.social{display:flex;align-items:center;gap:12px;color:#fff;font-size:12.5px;margin-bottom:12px}
.social i{width:30px;height:30px;border-radius:50%;border:1.5px solid #fff;display:inline-block}
.f-rule{left:141px;top:5195px;width:918px;height:1px;background:#3a4b70}
.copy{left:0;top:5218px;width:1200px;text-align:center;color:#fff;font-size:11.5px}
</style>
</head>
<body>

<!-- top bar -->
<div class="abs topbar">
  <span><i></i>Call now: (555) 014-2290</span>
  <span><i></i>Email: care@vardenhealth.com</span>
  <span><i></i>Time: Mon - Sun, 08:30am to 05:30pm</span>
</div>

<!-- header -->
<div class="abs brand">Varden Health</div>
<div class="abs brand-sub">SERVICES</div>
<nav class="abs nav">
  <a class="active" style="left:0">Home</a>
  <a style="left:76px">About Us</a>
  <a style="left:170px">Services ⌄</a>
  <a style="left:272px">Blog</a>
  <a style="left:339px">FAQs</a>
</nav>
<div class="abs btn-contact">Contact Now</div>

<!-- hero -->
<section class="abs hero" role="img" aria-label="Bright clinic room background"></section>
<div class="abs hero-person" role="img" aria-label="Smiling doctor in a white coat with arms crossed"></div>
<svg class="abs" style="left:0;top:600px" width="1200" height="150" viewBox="0 0 1200 150">
  <path d="M0,30 C180,40 380,150 600,140 C820,130 960,60 1200,110 L1200,150 L0,150 Z" fill="#fff"/>
</svg>
<div class="abs hero-eyebrow">COMPASSIONATE</div>
<h1 class="abs hero-title">MENTAL <span class="hl">WELLNESS</span> IN<br><span class="light">WASHINGTON DC</span></h1>
<p class="abs hero-text">Evidence-based care tailored to your needs. Where clinical expertise meets your unique needs</p>
<div class="abs btn-book">
  <svg width="13" height="13" viewBox="0 0 14 14"><rect x="1" y="2.5" width="12" height="10.5" rx="1.5" fill="none" stroke="#fff" stroke-width="1.5"/><path d="M1 6h12M4 1v3M10 1v3" stroke="#fff" stroke-width="1.5"/></svg>
  BOOK APPOINTMENT
</div>
<div class="abs scroll-btn">
  <svg width="20" height="22" viewBox="0 0 20 22"><path d="M10 2v17M3 12l7 7 7-7" fill="none" stroke="#f5883a" stroke-width="2" stroke-linecap="round"/></svg>
</div>

<!-- about -->
<div class="abs about-bubble"></div>
<div class="abs about-photo-main" role="img" aria-label="Portrait of a smiling woman with curly hair"></div>
<div class="abs about-photo-small" role="img" aria-label="Woman meditating on a sandy beach"></div>
<div class="abs kicker about-kicker">About</div>
<div class="abs headline about-head">Varden Health Services</div>
<p class="abs para" style="left:667px;top:920px;width:393px">Lorem ipsum dolor sit amet, consectetuer adipiscing elit sed diam nonummy nibh euismod tincidunt ut laoet dolo magna aliquam erat volutpat. Ut wisi enim ad minim m quis nostrud exerci tation ullamcorper suscipit lobortis nisl ut aliqip ea commodo consequat.</p>
<div class="abs sub-title" style="left:663px;top:1042px">
  <svg width="34" height="34" viewBox="0 0 34 34"><rect x="3" y="6" width="20" height="25" rx="2" fill="none" stroke="#0f1d3d" stroke-width="1.6"/><path d="M8 13h10M8 19h10M8 25h7" stroke="#0f1d3d" stroke-width="1.6"/><circle cx="25" cy="8" r="6" fill="#f5883a"/></svg>
  Our Mission
</div>
<p class="abs para" style="left:667px;top:1093px;width:393px">Lorem ipsum dolor sit amet, consectetuer adipiscing elit sed diam nonummy nibh euismod tincidunt ut laoet dolo magna aliquam erat volutpat. Ut wisi enim ad minim m quis nostrud exerci tation ullamcorper.</p>
<div class="abs sub-title" style="left:663px;top:1192px">
  <svg width="34" height="34" viewBox="0 0 34 34"><circle cx="15" cy="15" r="11" fill="none" stroke="#0f1d3d" stroke-width="1.6"/><circle cx="15" cy="15" r="5" fill="none" stroke="#0f1d3d" stroke-width="1.6"/><path d="M15 15l13-13" stroke="#f5883a" stroke-width="2.2"/><path d="M15 26v6M10 32h10" stroke="#0f1d3d" stroke-width="1.6"/></svg>
  Our Vision
</div>
<p class="abs para" style="left:667px;top:1243px;width:393px">Lorem ipsum dolor sit amet, consectetuer adipiscing elit sed diam nonummy nibh euismod tincidunt ut laoet dolo magna aliquam erat volutpat. Ut wisi enim ad minim m quis nostrud exerci tation ullamcorper.</p>

<!-- why choose us -->
<svg class="abs choose-bg" width="1200" height="750" viewBox="0 0 1200 750">
  <path d="M0,30 C120,0 240,60 380,55 C560,48 640,-10 820,20 C960,45 1080,100 1200,90 L1200,560 C1050,560 960,690 780,700 C560,712 420,640 260,650 C140,658 60,700 0,720 Z" fill="#a9dbe0"/>
</svg>
<div class="abs kicker choose-kicker">Choice</div>
<div class="abs headline choose-head">Why Choose Us</div>

<div class="abs feature-card" style="left:141px"><h3>Experienced<br>Therapists</h3><p>Our team consists of licensed professionals with years of experience in various mental health specialties.</p></div>
<div class="abs feature-tab" style="left:216px">
  <svg width="62" height="70" viewBox="0 0 62 70"><circle cx="31" cy="20" r="12" fill="none" stroke="#0f1d3d" stroke-width="2.4"/><path d="M8 66v-10c0-10 10-17 23-17s23 7 23 17v10z" fill="none" stroke="#0f1d3d" stroke-width="2.4"/><path d="M24 40l7 10 7-10" fill="none" stroke="#0f1d3d" stroke-width="2.2"/></svg>
</div>
<div class="abs feature-card" style="left:457px"><h3>Personalized<br>Approach</h3><p>We develop individualized treatment plans tailored to your unique needs and circumstances.</p></div>
<div class="abs feature-tab" style="left:532px">
  <svg width="74" height="74" viewBox="0 0 74 74"><circle cx="37" cy="37" r="32" fill="none" stroke="#0f1d3d" stroke-width="2.4" stroke-dasharray="40 10"/><circle cx="37" cy="37" r="20" fill="none" stroke="#0f1d3d" stroke-width="2.4"/><circle cx="37" cy="32" r="6" fill="none" stroke="#0f1d3d" stroke-width="2.2"/><path d="M26 49c2-7 20-7 22 0" fill="none" stroke="#0f1d3d" stroke-width="2.2"/></svg>
</div>
<div class="abs feature-card" style="left:771px"><h3>Flexible<br>Scheduling</h3><p>We offer evening and weekend appointments to accommodate your busy lifestyle.</p></div>
<div class="abs feature-tab" style="left:846px">
  <svg width="80" height="70" viewBox="0 0 80 70"><rect x="6" y="10" width="36" height="50" rx="3" fill="none" stroke="#0f1d3d" stroke-width="2.4"/><rect x="16" y="5" width="16" height="9" rx="2" fill="none" stroke="#0f1d3d" stroke-width="2.2"/><path d="M13 26h22M13 36h22M13 46h16" stroke="#0f1d3d" stroke-width="2.2"/><circle cx="56" cy="46" r="15" fill="#f7a566" stroke="#0f1d3d" stroke-width="2.4"/><path d="M56 38v9l6 4" fill="none" stroke="#0f1d3d" stroke-width="2.2"/></svg>
</div>

<!-- services -->
<div class="abs service-photo" role="img" aria-label="Woman in a standing yoga pose on a mountain ridge"></div>
<div class="abs kicker services-kicker">Offer</div>
<div class="abs headline services-head">Our Services</div>
<p class="abs para services-intro">Lorem ipsum dolor sit amet, consectetuer adipiscing elit sed diam nonummy nibh euismod tincidunt.</p>
<div class="abs service-panel">
  <div class="service-item">
    <svg width="64" height="56" viewBox="0 0 64 56"><circle cx="32" cy="12" r="6" fill="none" stroke="#f5883a" stroke-width="2"/><path d="M20 38l12-16 12 16M10 38h44M6 46h52" fill="none" stroke="#f5883a" stroke-width="2"/></svg>
    <div><h4>Individual Therapy</h4><p>Ut wisi enim ad minim veniam, quis nostrud exerci ullamcorper suscipit lobortis nisl ut aliquip ex ea commodo.</p></div>
  </div>
  <div class="service-item">
    <svg width="64" height="56" viewBox="0 0 64 56"><circle cx="20" cy="16" r="7" fill="none" stroke="#f5883a" stroke-width="2"/><circle cx="44" cy="16" r="7" fill="none" stroke="#f5883a" stroke-width="2"/><circle cx="32" cy="26" r="7" fill="none" stroke="#f5883a" stroke-width="2"/><path d="M6 44c2-9 9-13 14-13M58 44c-2-9-9-13-14-13M18 52c2-10 8-14 14-14s12 4 14 14" fill="none" stroke="#f5883a" stroke-width="2"/></svg>
    <div><h4>Group Therapy</h4><p>Ut wisi enim ad minim veniam, quis nostrud exerci ullamcorper suscipit lobortis nisl ut aliquip ex ea commodo.</p></div>
  </div>
  <div class="service-item">
    <svg width="64" height="56" viewBox="0 0 64 56"><circle cx="32" cy="18" r="11" fill="none" stroke="#f5883a" stroke-width="2"/><path d="M32 7v22M4 20l10 20 8 10M60 20l-10 20-8 10" fill="none" stroke="#f5883a" stroke-width="2"/></svg>
    <div><h4>Psychiatric Services</h4><p>Ut wisi enim ad minim veniam, quis nostrud exerci ullamcorper suscipit lobortis nisl ut aliquip ex ea commodo.</p></div>
  </div>
</div>

<!-- lake band -->
<div class="abs lake" role="img" aria-label="Person meditating on a wooden pier overlooking a mountain lake"></div>
<svg class="abs" style="left:0;top:2840px" width="1200" height="80" viewBox="0 0 1200 80">
  <path d="M0,0 L1200,0 L1200,20 C1000,60 800,10 600,35 C400,60 200,20 0,50 Z" fill="#fff"/>
</svg>

<!-- testimonials -->
<svg class="abs navy-band" width="1200" height="760" viewBox="0 0 1200 760">
  <path d="M0,40 C200,10 420,60 640,30 C860,0 1020,30 1200,10 L1200,700 C1000,740 820,690 620,720 C400,752 200,700 0,730 Z" fill="#0d1f45"/>
</svg>
<div class="abs t-kicker">Testimonials</div>
<div class="abs t-head">What Our Clients Say</div>

<div class="abs t-arrow" style="left:80px"><svg width="10" height="12" viewBox="0 0 10 12"><path d="M7 1L2 6l5 5" fill="none" stroke="#fff" stroke-width="1.6"/></svg></div>
<div class="abs t-arrow" style="left:1084px"><svg width="10" height="12" viewBox="0 0 10 12"><path d="M3 1l5 5-5 5" fill="none" stroke="#fff" stroke-width="1.6"/></svg></div>

<div class="abs t-card" style="left:141px"><p>"Lorem ipsum dolor sit amet, consectetuer adipiscing elit sed diam nonummy nibh euismod tincidunt ut laoet dolo magna aliquam erat volutpat. Ut wisi enim ad minim m quis nostrud exerci tation ullamcorper."</p><div class="stars">★★★★★</div></div>
<div class="abs t-quote" style="left:260px">“</div>
<div class="abs t-avatar" style="left:235px" role="img" aria-label="Client portrait"></div>
<div class="abs t-name" style="left:141px">Nadia Corwell<small>Wake County, NC</small></div>

<div class="abs t-card" style="left:461px"><p>"Lorem ipsum dolor sit amet, consectetuer adipiscing elit sed diam nonummy nibh euismod tincidunt ut laoet dolo magna aliquam erat volutpat. Ut wisi enim ad minim m quis nostrud exerci tation ullamcorper."</p><div class="stars">★★★★★</div></div>
<div class="abs t-quote" style="left:580px">“</div>
<div class="abs t-avatar" style="left:555px" role="img" aria-label="Client portrait"></div>
<div class="abs t-name" style="left:461px">Nadia Corwell<small>Wake County, NC</small></div>

<div class="abs t-card" style="left:784px"><p>"Lorem ipsum dolor sit amet, consectetuer adipiscing elit sed diam nonummy nibh euismod tincidunt ut laoet dolo magna aliquam erat volutpat. Ut wisi enim ad minim m quis nostrud exerci tation ullamcorper."</p><div class="stars">★★★★★</div></div>
<div class="abs t-quote" style="left:903px">“</div>
<div class="abs t-avatar" style="left:878px" role="img" aria-label="Client portrait"></div>
<div class="abs t-name" style="left:784px">Nadia Corwell<small>Wake County, NC</small></div>

<!-- contact -->
<div class="abs c-kicker">Contact us</div>
<div class="abs c-head"><span>Get in Touch</span></div>
<p class="abs para c-intro">Lorem ipsum dolor sit amet, consectetuer adipiscing elit sed diam nonummy nibh euismod tincidunt.</p>

<svg class="abs footer-bg" width="1200" height="694" viewBox="0 0 1200 694">
  <path d="M0,40 C200,70 380,20 600,40 C820,60 1000,0 1200,20 L1200,694 L0,694 Z" fill="#0d1f45"/>
</svg>

<form class="abs form-card">
  <div class="abs field" style="left:49px;top:61px;width:290px"><span class="ico"><svg width="11" height="11" viewBox="0 0 12 12"><circle cx="6" cy="3.5" r="2.8" fill="#9aa3b3"/><path d="M1 12c0-4 10-4 10 0z" fill="#9aa3b3"/></svg></span>First Name*</div>
  <div class="abs field" style="left:353px;top:61px;width:290px"><span class="ico"><svg width="11" height="11" viewBox="0 0 12 12"><circle cx="6" cy="3.5" r="2.8" fill="#9aa3b3"/><path d="M1 12c0-4 10-4 10 0z" fill="#9aa3b3"/></svg></span>Last Name*</div>
  <div class="abs field" style="left:49px;top:116px;width:290px"><span class="ico"><svg width="11" height="11" viewBox="0 0 12 12"><path d="M2 1l3 1 1 3-2 1c1 2 2 3 4 4l1-2 3 1 1 3c-6 1-12-5-11-11z" fill="#9aa3b3"/></svg></span>Your Phone*</div>
  <div class="abs field" style="left:353px;top:116px;width:290px"><span class="ico"><svg width="12" height="10" viewBox="0 0 12 10"><rect x="0.5" y="0.5" width="11" height="9" rx="1" fill="#9aa3b3"/><path d="M1 1l5 4 5-4" fill="none" stroke="#fff" stroke-width="1"/></svg></span>Your Email*</div>
  <div class="abs field area" style="left:49px;top:172px;width:594px"><span class="ico"><svg width="12" height="10" viewBox="0 0 12 10"><path d="M1 1h10v6H5l-3 2V7H1z" fill="#9aa3b3"/></svg></span><span>Your Message</span></div>
</form>
<div class="abs btn-submit">Submit Now <i><svg width="8" height="10" viewBox="0 0 8 10"><path d="M2 1l4 4-4 4" fill="none" stroke="#0f1d3d" stroke-width="1.6"/></svg></i></div>

<!-- footer -->
<div class="abs sub-script">Subscribe</div>
<div class="abs sub-title-f">Stay Up To Date!</div>
<div class="abs sub-input"><span>Enter Your Email Here</span><b>Subscribe Now <i>›</i></b></div>

<div class="abs f-col" style="left:141px;top:4924px">
  <h5>Quick Links</h5>
  <ul><li>• Home</li><li>• About Us</li><li>• Services</li><li>• Our Team</li><li>• Contact Us</li></ul>
</div>
<div class="abs f-col" style="left:369px;top:4924px;width:250px">
  <h5>Contact Details</h5>
  <div class="det"><svg width="13" height="16" viewBox="0 0 13 16"><path d="M6.5 1a5 5 0 0 1 5 5c0 4-5 9-5 9s-5-5-5-9a5 5 0 0 1 5-5z" fill="#fff"/><circle cx="6.5" cy="6" r="2" fill="#0d1f45"/></svg><div><b>ADDRESS</b><br>123 Ut Wisi Enim Ad Minim<br>Veniam Quis, California.</div></div>
  <div class="det"><svg width="13" height="13" viewBox="0 0 12 12"><path d="M2 1l3 1 1 3-2 1c1 2 2 3 4 4l1-2 3 1 1 3c-6 1-12-5-11-11z" fill="#fff"/></svg><div><b>PHONE</b><br>555 014 2290</div></div>
  <div class="det"><svg width="14" height="11" viewBox="0 0 12 10"><rect x="0.5" y="0.5" width="11" height="9" rx="1" fill="#fff"/><path d="M1 1l5 4 5-4" fill="none" stroke="#0d1f45" stroke-width="1"/></svg><div><b>EMAIL</b><br>info@vardenhealth.com</div></div>
</div>
<div class="abs f-col" style="left:673px;top:4924px">
  <h5>Follow Us</h5>
  <div class="social"><i></i>Linkroom</div>
  <div class="social"><i></i>Streamly</div>
  <div class="social"><i></i>Picboard</div>
  <div class="social"><i></i>Postline</div>
</div>

<div class="abs f-rule"></div>
<div class="abs copy">© 2025 Varden Health Services. All Rights Reserved.</div>

</body>
</html>
```